New Osteopathy Clinic needs a flyer design

New osteopathy clinic in West London. We help patients generally with musculoskeletal pain such as low back pain, neck and shoulder pain, headaches, arthritis etc. The osteopath also is registered in medical acupuncture. The design is to attract business professionals and the public alike. The final design should communicate warmth and trust.
Updates

Project Deadline Extended
Reason: The clinic still has a few weeks until launch so I have extended the deadline. Thanks

Target Market(s)

Professionals and general public in a generally afluent neighbourhood, with big businesses close by

Industry/Entity Type

Alternative Medicine

Font styles to use
Serif
Sans Serif
Other font styles liked:
• Arial

Requirements
Must have
• Provide information about osteopathy and conditions treated.
• Address: 41 Tarrowby Lane, Shepherds Bush W12 3QE
• Cost: £50 initial consultation, 40 mins. Subsequent treatments 30 mins, same price.
• Initial offer: KMR, DJ students and Brookhaven Plaza employees 25% discount with leaflet.
Nice to have
• As a natural therapy and holistic clinic, maybe some imagery that reflects that.
• Double sided A5 size would be nice.
• Mentioning that poor ergonomics and posture from seated jobs all day can predispose to pain, especially low back pain, neck pain and headaches.
Should not have
• Arty Flowery Designs and fonts

```html
<!DOCTYPE html>
<html lang="en">
<head>
<meta charset="utf-8">
<title>Restwell Osteopathy Clinic – Leaflet</title>
<link href="https://fonts.googleapis.com/css2?family=Arimo:wght@400;700&display=swap" rel="stylesheet">
<style>
  :root {
    --blue: #1ba1da;
    --blue-dark: #0f7fb3;
    --ink: #3a3a3a;
    --grey: #6b6b6b;
    --paper: #ffffff;
    --page: #ffffff;
    --skin: #d9b9a6;
    --mist: #e9e9e9;
  }
  * { box-sizing: border-box; margin: 0; padding: 0; }
  html, body { width: 811px; height: 1200px; overflow: hidden; background: var(--page); }
  body { position: relative; font-family: 'Arimo', Arial, sans-serif; color: var(--ink); }

  .side { position: absolute; left: 30px; width: 751px; background: var(--paper); overflow: hidden;
          box-shadow: 0 0 0 1px #dcdcdc; }
  .side--front { top: 27px; height: 535px; }
  .side--back  { top: 600px; height: 528px;
                 background: linear-gradient(90deg, #f4f4f4 0%, #e2e2e2 45%, #cfcfcf 100%); }

  .brand { position: absolute; left: 22px; top: 22px; display: flex; align-items: flex-start; gap: 12px; }
  .brand__dot { width: 22px; height: 22px; border-radius: 50%; background: var(--blue); margin-top: 22px; }
  .brand__name { font-size: 66px; line-height: 1; color: var(--grey); letter-spacing: -1px; }
  .brand__tag { display: block; font-size: 25px; color: var(--grey); letter-spacing: 0; margin-top: 4px; padding-left: 56px; }

  .photo { position: absolute; }
  .photo--back-pain { right: 0; top: 0; width: 430px; height: 478px;
    background: linear-gradient(135deg, #f5ece6 0%, var(--skin) 55%, #b98b76 100%); }
  .photo--headache { right: 0; top: 0; width: 420px; height: 478px;
    background: linear-gradient(90deg, rgba(220,220,220,0) 0%, #bdbdbd 35%, #9a9a9a 100%); }

  .offer { position: absolute; left: 560px; top: 6px; width: 170px; height: 170px; border-radius: 50%;
           background: var(--blue); color: #fff; text-align: center; padding-top: 22px; }
  .offer__kicker { font-size: 11px; font-weight: 700; line-height: 1.2; text-transform: uppercase; }
  .offer__value { font-size: 54px; font-weight: 700; line-height: 1; }
  .offer__label { font-size: 18px; font-weight: 700; letter-spacing: 1px; }
  .offer__terms { font-size: 10px; line-height: 1.25; margin: 3px 22px 0; }

  .intro { position: absolute; left: 24px; top: 140px; width: 300px; font-size: 14px; line-height: 1.35; }
  .conditions { position: absolute; left: 24px; top: 228px; font-size: 14px; line-height: 1.38; }
  .conditions ul { list-style: none; margin-top: 2px; }
  .conditions li::before { content: ""; display: inline-block; width: 7px; height: 7px; border-radius: 50%;
                           background: var(--blue); margin-right: 7px; vertical-align: 1px; }

  .thumbs { position: absolute; display: flex; gap: 8px; }
  .thumb { width: 78px; height: 60px; }
  .side--front .thumbs { left: 180px; top: 400px; }
  .side--front .thumb { background: linear-gradient(135deg, #eee, #b9b9b9); }
  .side--back .thumbs { left: 440px; top: 402px; }
  .side--back .thumb { width: 86px; height: 66px; border: 3px solid var(--blue);
                       background: linear-gradient(135deg, #f1f1f1, #aeb8bd); }

  .accred { position: absolute; left: 180px; top: 466px; font-size: 12px; }
  .accred::before { content: ""; display: inline-block; width: 7px; height: 7px; border-radius: 50%;
                    background: var(--blue); margin-right: 6px; }

  .band { position: absolute; left: 0; right: 0; bottom: 0; height: 57px; background: var(--blue); color: #fff;
          text-align: center; display: flex; flex-direction: column; justify-content: center; }
  .band__name { font-size: 18px; font-weight: 700; }
  .band__addr { font-size: 14px; margin-top: 3px; }
  .side--back .band { height: 50px; font-size: 12.5px; }
  .band b { font-weight: 700; }

  .pitch { position: absolute; left: 20px; top: 170px; width: 320px; text-align: center;
           font-size: 17px; line-height: 1.3; color: var(--ink); }
  .pitch p + p { margin-top: 14px; }

  .note { position: absolute; left: 34px; top: 1140px; font-size: 14px; color: var(--grey); letter-spacing: .5px; }
</style>
</head>
<body>

<section class="side side--front">
  <div class="photo photo--back-pain" role="img" aria-label="Photo of a woman holding her lower back in pain"></div>

  <div class="brand">
    <span class="brand__dot"></span>
    <div class="brand__name">Restwell<span class="brand__tag">osteopathy clinic</span></div>
  </div>

  <div class="offer">
    <div class="offer__kicker">Special<br>opening offer</div>
    <div class="offer__value">25%</div>
    <div class="offer__label">DISCOUNT</div>
    <div class="offer__terms">for KMR, DJ students and Brookhaven Plaza employees with this leaflet</div>
  </div>

  <p class="intro">Poor ergonomics and posture from seated jobs all day can predispose to pain, especially low back pain, neck pain and headaches.</p>

  <div class="conditions">
    <p>We have treatments for:</p>
    <ul>
      <li>Arthritis</li>
      <li>Back Pain</li>
      <li>Foot and Ankle Pain</li>
      <li>Hand and Elbow Pain</li>
      <li>Headaches</li>
      <li>Hip Pain</li>
      <li>Knee Pain</li>
      <li>Neck Pain</li>
      <li>Shoulder Pain</li>
      <li>Tennis/Golfers Elbow</li>
    </ul>
  </div>

  <div class="thumbs">
    <div class="thumb" role="img" aria-label="Photo of a back treatment"></div>
    <div class="thumb" role="img" aria-label="Photo of a neck treatment"></div>
    <div class="thumb" role="img" aria-label="Photo of acupuncture needles"></div>
  </div>
  <p class="accred">Registered in Medical Acupuncture</p>

  <footer class="band">
    <span class="band__name">Restwell Osteopathy Clinic</span>
    <span class="band__addr">41 Tarrowby Lane, Shepherds Bush W12 3QE Tel: 0100 555 0192</span>
  </footer>
</section>

<section class="side side--back">
  <div class="photo photo--headache" role="img" aria-label="Black and white photo of a woman holding her head with a headache"></div>

  <div class="brand">
    <span class="brand__dot"></span>
    <div class="brand__name">Restwell<span class="brand__tag">osteopathy clinic</span></div>
  </div>

  <div class="pitch">
    <p>From headaches to foot pain and everything in between, people are choosing West London's newest osteopathy clinic for all kinds of reasons, but mainly because they get results!</p>
    <p>Discover the widest range of Complementary &amp; Contemporary Therapies narrowed down to one call. Tel: 0100 555 0192 www.restwellosteopathy.co.uk</p>
  </div>

  <div class="thumbs">
    <div class="thumb" role="img" aria-label="Photo of a spine model"></div>
    <div class="thumb" role="img" aria-label="Photo of a shoulder treatment"></div>
    <div class="thumb" role="img" aria-label="Photo of a relaxed patient"></div>
  </div>

  <footer class="band">
    <span><b>£50 for an initial 40 minute consultation.</b> Subsequent treatments 30 minutes for the same price.</span>
  </footer>
</section>

<p class="note">2 SIDED AS LEAFLET</p>

</body>
</html>
```